Events and Parties web-site needs a Web Design

ZorVeno needs a web design.
ZorVeno means The Bees in Italian.
ZorVeno target market is people who is organizing parties and events.
Our mission is that the parties and events of our clients exceed their expectations by providing them web and mobile tools.
Our vision is to be the best and biggest party web portal of the country.
The main features of our web site is to let people invite guests and search suppliers/providers. Guests will also confirm presence (RSVP) and buy presents/gifts at the site as well.
Our slogan is "Curta sua festa desde já !" that means "Enjoy our party now !" in Brazilian Portuguese.
The idea here is that the party starts now and not only at the scheduled date and time.
Updates
It seems that must have and nice to have briefing is not appearing to you as I filled. So I will type it agai here:
Our slogan text that is "Curta sua festa desde já !" that means "Enjoy your party now !".
Space to paid ads.
Language switch to Spanish. Brazilian Portuguese is our default language.
Logon form with 2 inputs: Email and password.
RSVP form with 2 inputs: Event ID and password
Plivex trusted site seal (SSL/HTTPS) logo.
Update to my briefing: Only event organizer and guests will be able to see details of the events/parties like photos/blog, guest list and etc. Suppliers will be searched and rated like stayvorta.com/wandrikel.
Target Market(s)
ZorVeno target market is amateur and professional people who are organizing parties and events.
Our mission is that the parties and events of our clients exceed their expectations by providing them easy and fast web and mobile tools.
Our vision is to be the best and biggest party portal of our country.
The main features of our web site is to let people invite guests and search suppliers/providers. Guests will also confirm presence (RSVP) and buy presents at the site.
Industry/Entity Type
Events
Requirements
Must have
- Design and colors compliant with attached logo.
- Our slogan text that is "Curta sua festa desde já !" that means "Enjoy your party now !".
- Space to paid ads.
- Language switch to Spanish. Brazilian Portuguese is our default language.
- Logon form with 2 inputs: Email and password.
- RSVP form with 2 inputs: Event ID and password
- Plivex trusted site seal (SSL/HTTPS) logo.
Nice to have
- ZorVeno stands for The Bees in Italian. It would be very nice to have a not so explicit idea that each user is a bee and ZorVeno is the hive where party/event occurs.
Should not have
- No PageMolder please.
- No infant/child oriented designs please. Our market is not only children birthdays but also other parties and events like marriages, corporate events and so on

```html
<!DOCTYPE html>
<html lang="pt-BR">
<head>
<meta charset="utf-8">
<title>ZorVeno — Curta sua festa desde já !</title>
<link href="https://fonts.googleapis.com/css2?family=Merriweather:wght@400;700&family=Open+Sans:wght@400;600;700&display=swap" rel="stylesheet">
<style>
:root{
  --backdrop:#d3d9dc;
  --page:#ffffff;
  --hero-bg:#f1f1f1;
  --gold:#f5b50f;
  --gold-light:#f5c048;
  --amber-1:#e0a10a;
  --amber-2:#d89a08;
  --amber-3:#e6a70c;
  --amber-4:#fbbb12;
  --maroon:#3d0b0b;
  --tour:#4a1111;
  --mauve:#6e5a5a;
  --footer:#a87800;
  --footer-bar:#efb419;
  --text:#555555;
  --text-dark:#333333;
  --line:#ececec;
  --field:#e2e2e2;
  --accent-text:#f0a500;
  --serif:'Merriweather', Georgia, serif;
  --sans:'Open Sans', Arial, sans-serif;
}
*{box-sizing:border-box;margin:0;padding:0}
html,body{width:954px;height:1200px;overflow:hidden}
body{background:radial-gradient(ellipse at 50% 40%,#eef1f2 0%,var(--backdrop) 75%);font-family:var(--sans);color:var(--text);position:relative}
.page{position:absolute;left:107px;top:110px;width:732px;height:1028px;background:var(--page);box-shadow:0 6px 24px rgba(0,0,0,.18);overflow:hidden}
.abs{position:absolute}
/* hero band */
.hero-band{left:0;top:0;width:732px;height:365px;background:linear-gradient(120deg,#f3f3f3 0%,#ececec 60%,#f4f4f4 100%)}
/* top bar */
.topbar{left:137px;top:0;width:458px;height:14px;background:var(--gold);color:#fff;font-size:5.5px;font-weight:700;display:flex;align-items:center;justify-content:space-between;padding:0 14px}
.topbar .links span{margin-right:5px}
.topbar .contact span{margin-left:10px}
.header{left:137px;top:14px;width:458px;height:48px;background:#fff}
.brand{position:absolute;left:5px;top:10px;display:flex;align-items:center;gap:4px;font-family:var(--sans);font-weight:600;font-size:13px;color:var(--text-dark)}
.brand i{display:block;width:10px;height:10px;border-radius:50%;background:var(--gold)}
.social{position:absolute;right:14px;top:17px;display:flex;gap:3px}
.social i{display:block;width:13px;height:13px;border-radius:50%;background:#9a8585}
.nav{left:137px;top:62px;width:458px;height:24px;background:#fff;border-top:1px solid var(--line);border-bottom:1px solid var(--line);display:flex;font-size:6.5px;font-weight:600;color:var(--text-dark)}
.nav a{display:flex;align-items:center;padding:0 13px;border-right:1px solid var(--line);text-decoration:none;color:inherit;height:100%}
.nav a.active{border-bottom:2px solid var(--gold)}
.nav a.muted{color:#999;border-right:none}
.nav .search{margin-left:auto;width:24px;display:flex;align-items:center;justify-content:center}
/* slider */
.slogan{font-family:var(--serif);color:#fff;font-size:13.5px;padding:0 7px;line-height:26px;height:26px}
.slogan.pt{left:137px;top:177px;background:var(--gold-light)}
.slogan.en{left:137px;top:203px;background:var(--mauve);height:27px;line-height:27px}
.photo{left:398px;top:128px;width:197px;height:194px;background:radial-gradient(ellipse at 45% 45%,#b58a62 0%,#d9c3ad 45%,#ececec 75%)}
.arrow{top:176px;width:27px;height:55px;background:#fff;display:flex;align-items:center;justify-content:center}
.arrow.left{left:0;border-right:2px solid #333}
.arrow.right{right:0;border-left:2px solid #333}
/* tiles */
.tiles{left:137px;top:322px;width:458px;height:87px;display:flex}
.tile{flex:1;display:flex;flex-direction:column;align-items:center;justify-content:center;gap:8px;color:#fff;font-family:var(--serif);font-weight:700;font-size:8px}
.tile .ic{width:33px;height:33px;border-radius:50%;background:#fff;display:flex;align-items:center;justify-content:center}
.t1{background:var(--amber-1)}.t2{background:var(--amber-2)}.t3{background:var(--amber-3)}.t4{background:var(--amber-4)}.t5{background:var(--tour)}
/* columns */
.cols{left:137px;top:409px;width:458px;height:429px;display:flex;border-left:1px solid var(--line);border-right:1px solid var(--line)}
.col{position:relative;height:100%}
.col-left{width:126px;border-right:1px solid var(--line)}
.col-mid{width:206px;border-right:1px solid var(--line)}
.col-right{width:126px}
.bar{position:absolute;height:15px;background:var(--gold);color:var(--text-dark);font-family:var(--serif);font-weight:700;font-size:6.3px;display:flex;align-items:center;justify-content:space-between;padding:0 5px}
.bar.dark{background:var(--maroon);color:#fff}
.bar.gold-white{color:#fff}
.pager{display:flex;gap:2px}
.pager i{width:8px;height:8px;border-radius:50%;background:#fff;border:1px solid #444;display:block}
.copy{position:absolute;font-size:6.3px;line-height:11px;color:var(--text-dark)}
.field{position:absolute;height:16px;border:1px solid var(--field);background:#fff;font-size:5px;color:#bbb;padding-left:4px;display:flex;align-items:center}
.btn{position:absolute;height:16px;border:1px solid var(--field);background:#fff;font-size:5.5px;font-weight:700;color:var(--text-dark);display:flex;align-items:center;justify-content:center}
.seal{position:absolute;left:13px;top:404px;width:27px;height:20px;background:#e8e8e8;border:1px solid #ccc}
.divider{position:absolute;height:1px;background:var(--line)}
.news{position:absolute;left:14px;width:178px}
.news .avatar{position:absolute;left:0;top:3px;width:32px;height:32px;border-radius:50%;background:#efefef}
.news h4{margin-left:40px;font-size:6.5px;font-weight:600;color:var(--text-dark)}
.news .date{margin-left:40px;font-size:5px;color:#999;margin-top:1px}
.news p{margin-left:40px;font-size:6px;line-height:10.5px;color:var(--text-dark);margin-top:2px}
.video{position:absolute;left:14px;top:251px;width:178px;height:112px;background:#efefef}
.ad{position:absolute;left:26px;width:72px;height:22px;background:#f1f1f1}
.event{position:absolute;left:13px;width:110px;height:30px}
.event .badge{position:absolute;left:0;top:0;width:24px;text-align:center}
.event .mo{background:var(--mauve);color:#fff;font-size:5px;font-weight:700;height:10px;line-height:10px}
.event .day{border:1px solid #ddd;border-top:none;font-size:10px;color:var(--text-dark);height:18px;line-height:17px}
.event h5{position:absolute;left:32px;top:0;font-size:6.5px;font-weight:600;color:var(--accent-text);line-height:9.5px;width:70px}
.event small{position:absolute;left:32px;top:21px;font-size:5px;color:#777}
/* footer */
.footer{left:0;top:838px;width:732px;height:190px;background:var(--footer)}
.fcol{position:absolute;top:31px;color:#fff}
.fcol h3{font-family:var(--serif);font-weight:700;font-size:6.5px;padding-bottom:5px;position:relative}
.fcol h3::after{content:"";position:absolute;left:0;bottom:0;width:20px;height:1px;background:#fff}
.fcol p{font-size:6px;line-height:11px;margin-top:11px}
.tags{display:flex;flex-wrap:wrap;gap:4px;width:90px;margin-top:12px}
.tags span{background:var(--maroon);color:#fff;font-size:5.8px;padding:0 5px;height:15px;line-height:15px}
.tweet{font-size:5.8px;font-style:italic;line-height:10px;margin-top:11px}
.tweet b{color:var(--maroon);font-weight:600}
.tweet small{display:block;font-style:normal;font-size:5px;margin-top:2px}
.gallery{display:grid;grid-template-columns:repeat(3,30px);gap:4px;margin-top:12px}
.gallery i{display:block;width:30px;height:30px;background:#e8e8e8}
.fbar{left:151px;top:1004px;width:430px;height:24px;background:var(--footer-bar);color:#fff;font-size:5.5px;display:flex;align-items:center;justify-content:space-between;padding:0 8px}
</style>
</head>
<body>
<main class="page">
  <div class="abs hero-band"></div>

  <div class="abs topbar">
    <div class="links"><span>Link</span><span>Link</span><span>Link</span><span>Link</span><span>Link</span></div>
    <div class="contact"><span>☎ 1800-555-0147</span><span>✉ hello@zorveno-mail.net</span></div>
  </div>
  <header class="abs header">
    <div class="brand"><i></i>ZorVeno</div>
    <div class="social"><i></i><i></i><i></i><i></i><i></i></div>
  </header>
  <nav class="abs nav">
    <a class="active">Home</a><a>About Us</a><a>Courses ▾</a><a>Events</a><a>News</a><a>Gallery</a><a class="muted">Contact Us</a>
    <span class="search"><svg width="8" height="8" viewBox="0 0 10 10"><circle cx="4" cy="4" r="3" fill="none" stroke="#bbb" stroke-width="1.3"/><path d="M6.3 6.3 9 9" stroke="#bbb" stroke-width="1.3"/></svg></span>
  </nav>

  <div class="abs arrow left"><svg width="8" height="14" viewBox="0 0 8 14"><path d="M7 1 1 7l6 6" fill="none" stroke="#f5b50f" stroke-width="1.5"/></svg></div>
  <div class="abs arrow right"><svg width="8" height="14" viewBox="0 0 8 14"><path d="M1 1l6 6-6 6" fill="none" stroke="#f5b50f" stroke-width="1.5"/></svg></div>
  <div class="abs slogan pt">Curta sua festa desde já !</div>
  <div class="abs slogan en">Enjoy our party now !</div>
  <div class="abs photo" role="img" aria-label="Photo of a smiling woman with long wavy hair leaning on her arms"></div>

  <section class="abs tiles">
    <div class="tile t1"><span class="ic"><svg width="16" height="16" viewBox="0 0 16 16"><path d="M8 14 2 8a3.3 3.3 0 0 1 6-4 3.3 3.3 0 0 1 6 4z" fill="#e0a10a"/></svg></span>Link</div>
    <div class="tile t2"><span class="ic"><svg width="16" height="16" viewBox="0 0 16 16"><path d="M3 13l1-4 7-7 3 3-7 7z" fill="#d89a08"/></svg></span>Link</div>
    <div class="tile t3"><span class="ic"><svg width="16" height="16" viewBox="0 0 16 16"><path d="M8 1l2.1 4.5 4.9.5-3.7 3.3 1.1 4.8L8 11.6 3.6 14.1l1.1-4.8L1 6l4.9-.5z" fill="#e6a70c"/></svg></span>Link</div>
    <div class="tile t4"><span class="ic"><svg width="16" height="16" viewBox="0 0 16 16"><path d="M8 2 1 8h2v6h4v-4h2v4h4V8h2z" fill="#fbbb12"/></svg></span>Link</div>
    <div class="tile t5"><span class="ic"><svg width="14" height="12" viewBox="0 0 14 12"><rect width="14" height="12" rx="3" fill="#f5b50f"/><path d="M5.5 3.5v5l4-2.5z" fill="#fff"/></svg></span>Take a Tour</div>
  </section>

  <section class="abs cols">
    <div class="col col-left">
      <div class="bar" style="left:13px;top:12px;width:98px">R.S.V.P. »</div>
      <p class="copy" style="left:13px;top:36px;width:100px">Li Europan lingues es membres del sam familie.</p>
      <div class="field" style="left:13px;top:65px;width:98px">Event ID</div>
      <div class="field" style="left:13px;top:86px;width:98px">Password</div>
      <div class="btn" style="left:79px;top:107px;width:32px">Search</div>
      <div class="divider" style="left:0;top:137px;width:125px"></div>
      <div class="bar" style="left:13px;top:145px;width:98px">Log In »</div>
      <p class="copy" style="left:13px;top:169px;width:100px">Li Europan lingues es membres del sam familie.</p>
      <div class="field" style="left:13px;top:198px;width:98px">Email</div>
      <div class="field" style="left:13px;top:219px;width:98px">Password</div>
      <div class="btn" style="left:78px;top:240px;width:33px">Go</div>
      <div class="divider" style="left:0;top:263px;width:125px"></div>
      <div class="bar dark" style="left:13px;top:275px;width:98px">Newsletter »</div>
      <p class="copy" style="left:13px;top:300px;width:100px">Li Europan lingues es membres del sam familie.</p>
      <div class="field" style="left:13px;top:328px;width:98px">Email Address</div>
      <div class="btn" style="left:70px;top:350px;width:41px">Subscribe</div>
      <div class="seal"></div>
    </div>

    <div class="col col-mid">
      <div class="bar" style="left:14px;top:12px;width:178px;color:#fff"><span>News »</span><span class="pager"><i></i><i></i></span></div>
      <article class="news" style="top:37px"><span class="avatar"></span><h4>To an English person, it will seem like simply</h4><div class="date">Feb 13th, 2014</div><p>A un Angleso it va semblar un simplificat Angles</p></article>
      <div class="divider" style="left:54px;top:88px;width:138px"></div>
      <article class="news" style="top:96px"><span class="avatar"></span><h4>To an English person, it will seem like simply</h4><div class="date">Feb 13th, 2014</div><p>A un Angleso it va semblar un simplificat Angles</p></article>
      <div class="divider" style="left:54px;top:147px;width:138px"></div>
      <article class="news" style="top:155px"><span class="avatar"></span><h4>To an English person, it will seem like simply</h4><div class="date">Feb 13th, 2014</div><p>A un Angleso it va semblar un simplificat Angles</p></article>
      <div class="divider" style="left:0;top:210px;width:205px"></div>
      <div class="bar dark" style="left:14px;top:225px;width:178px"><span>Video Tour »</span><span class="pager"><i></i><i></i></span></div>
      <div class="video" role="img" aria-label="Video tour player"></div>
      <p class="copy" style="left:14px;top:369px;width:170px">It wasn't a dream. His room, a proper human room although a little too small</p>
    </div>

    <div class="col col-right">
      <div class="bar gold-white" style="left:13px;top:13px;width:98px"><span>Sponsors »</span><span class="pager"><i></i><i></i></span></div>
      <div class="ad" style="top:40px"></div>
      <div class="ad" style="top:71px"></div>
      <div class="ad" style="top:103px"></div>
      <div class="divider" style="left:0;top:149px;width:125px"></div>
      <div class="bar gold-white" style="left:13px;top:170px;width:98px">Save the Date »</div>
      <div class="event" style="top:197px"><div class="badge"><div class="mo">FEB</div><div class="day">08</div></div><h5>The new common will be more simple</h5><small>9:00am to 1:00pm</small></div>
      <div class="event" style="top:235px"><div class="badge"><div class="mo">FEB</div><div class="day">10</div></div><h5>The new common will be more simple</h5><small>9:00am to 1:00pm</small></div>
      <div class="event" style="top:273px"><div class="badge"><div class="mo">FEB</div><div class="day">14</div></div><h5>The new common will be more simple</h5><small>9:00am to 1:00pm</small></div>
    </div>
  </section>

  <footer class="abs footer">
    <div class="fcol" style="left:151px;width:100px"><h3>About Us</h3><p>Quisque bibendum erat feugiat rhoncus tincidunt ipsum mi facilisis nisl, nec eleifend enim massa ac purus. Integer malesuada faucibus auctor vivamus accumsan justo.</p></div>
    <div class="fcol" style="left:262px"><h3>Tag Cloud</h3><div class="tags"><span>Education</span><span>Funny</span><span>College</span><span>Parties</span><span>Art</span><span>Design</span><span>Music</span><span>March</span></div></div>
    <div class="fcol" style="left:373px;width:92px"><h3>Chirpline Feed</h3>
      <div class="tweet"><b>@ZorVeno</b> imperdiet adipiscing elit ac fermentum. nullam et<small>about 6 hours ago</small></div>
      <div class="tweet"><b>@ZorVeno</b> imperdiet adipiscing elit ac fermentum. nullam et<small>about 6 hours ago</small></div>
    </div>
    <div class="fcol" style="left:483px"><h3>&nbsp;Photo Gallery »</h3><div class="gallery"><i></i><i></i><i></i><i></i><i></i><i></i></div></div>
  </footer>
  <div class="abs fbar"><span>© Copyright <b style="color:var(--maroon);font-weight:600">ZorVeno</b></span><span>Top ⌃</span></div>
</main>
</body>
</html>
```